Business Card Design Project

We need a business card design for a consultancy called 'Amber Ridge'. The design should communicate innovation and professionalism. The colors used should complement our logo. Please include source files for winning design.
Updates

Industry/Entity Type

Business

Colors

Designer to choose colors to be used in the design.

Requirements
Must have
• Card size should be 85mm x 50mm. The back side of the card should be the logo on a black background. The front side should display the name 'Amber Ridge' along with standard information. The front's design should graphically complement the back.
Nice to have
• Any graphical elements in the front the complement the back side (with the logo on a black background) would be a plus.

```html
<!DOCTYPE html>
<html lang="en">
<head>
<meta charset="utf-8">
<title>Amber Ridge — Business Card</title>
<link rel="stylesheet" href="https://fonts.googleapis.com/css2?family=Cinzel:wght@400;600&family=Open+Sans:wght@300;400&display=swap">
<style>
  :root {
    --backdrop: #1d1d1d;
    --card-black: #050505;
    --amber: #f39a2b;
    --amber-light: #f6d98f;
    --shade-top: #060606;
    --shade-bottom: #1c1c1c;
  }
  * { margin: 0; padding: 0; box-sizing: border-box; }
  html, body {
    width: 1200px;
    height: 873px;
    overflow: hidden;
    background: var(--backdrop);
  }
  .stage {
    width: 1200px;
    height: 873px;
    display: flex;
    align-items: center;
    justify-content: center;
    gap: 60px;
  }
  .card {
    position: relative;
    width: 510px;
    height: 300px;
    background: var(--card-black);
    overflow: hidden;
    box-shadow: 0 10px 30px rgba(0,0,0,0.5);
  }

  /* Front */
  .card-front .brand-name {
    position: absolute;
    top: 26px;
    right: 34px;
    font-family: "Cinzel", serif;
    font-weight: 600;
    font-size: 50px;
    letter-spacing: 1px;
    color: var(--amber-light);
    white-space: nowrap;
  }
  .card-front .rule {
    position: absolute;
    inset: 0;
  }
  .card-front .contact {
    position: absolute;
    top: 122px;
    left: 64px;
    font-family: "Open Sans", sans-serif;
    font-weight: 300;
    font-size: 13px;
    line-height: 1.45;
    color: var(--amber-light);
    list-style: none;
  }
  .card-front .scene-area {
    position: absolute;
    right: 0;
    bottom: 0;
    width: 260px;
    height: 150px;
    background: linear-gradient(180deg, var(--shade-top) 0%, var(--shade-bottom) 100%);
  }

  /* Back */
  .card-back .emblem {
    position: absolute;
    top: 40px;
    left: 50%;
    transform: translateX(-50%);
    width: 160px;
    height: 160px;
    border-radius: 50%;
    background: radial-gradient(circle at 55% 45%, var(--amber-light), var(--amber));
  }
  .card-back .brand-name {
    position: absolute;
    top: 214px;
    left: 0;
    right: 0;
    text-align: center;
    font-family: "Cinzel", serif;
    font-weight: 600;
    font-size: 24px;
    letter-spacing: 1px;
    color: var(--amber-light);
  }
  .card-back .corner-accent {
    position: absolute;
    left: 0;
    bottom: 0;
  }
</style>
</head>
<body>
<main class="stage">
  <section class="card card-front" aria-label="Card front">
    <div class="scene-area" role="img" aria-label="Dark coastal scene with a lighthouse"></div>
    <svg class="rule" width="510" height="300" viewBox="0 0 510 300" aria-hidden="true">
      <line x1="36" y1="100" x2="510" y2="100" stroke="var(--amber)" stroke-width="2"/>
      <line x1="36" y1="100" x2="0" y2="150" stroke="var(--amber)" stroke-width="2"/>
    </svg>
    <h1 class="brand-name">Amber Ridge</h1>
    <ul class="contact">
      <li>hello@amberridge.com</li>
      <li>www.amberridge.com</li>
      <li>067-555-2741</li>
    </ul>
  </section>

  <section class="card card-back" aria-label="Card back">
    <div class="emblem" aria-hidden="true"></div>
    <p class="brand-name">Amber Ridge</p>
    <svg class="corner-accent" width="120" height="60" viewBox="0 0 120 60" aria-hidden="true">
      <polygon points="0,60 0,14 120,60" fill="var(--amber)"/>
    </svg>
  </section>
</main>
</body>
</html>
```